VORELLO - PIZZA - RESTAURANT PIZZERIA

Flyer format:
- A5 front / back leaflet (Example attachment)
Customer logos:
- Attachment, VORELLO PIZZA logo
Address and contact to put on the flyers:
- Phone to add: (+352) 26 58 40 71 (Page 1)
- Address to be added: 27 rue des tilleuls, L-3829 Kayl, Luxembourg (Page 1)
- Website: www.vorello-example.lu (Page 1)
- Leave a space for the timetable (last page)
Flyer color:
- Preferably black background with colored customer logo
Typefaces:
- At your convenience
Descriptions:
- We would like to have a flyer to the one we have put as an example in the attachment
Important elements:
- Pizza oven on the cover page with customer logo, address and contact details
- The graphic elements must be usable and non-paying, we want a quality visual.
- Menu (attachment) The menu is in Word format, it must be laid out in a thoughtful way as on the example model.
- We need to find some pizza and/or ingredient visuals
Aspects :
- The design of the set must be elegant, sober and must contain all the information (Menu, visual of your choice, logo)

Target Market(s)

Private and professional public

Font styles to use
Serif
Sans Serif

Requirements
Must have
• Elegance, take into account the information of the comment
Nice to have
• Pizza oven, Dominant color black, Gold, red
Should not have
• poor quality visuals

```html
<!DOCTYPE html>
<html lang="fr">
<head>
<meta charset="utf-8">
<title>Vorello Pizza – Menu</title>
<link href="https://fonts.googleapis.com/css2?family=Poppins:ital,wght@0,400;0,600;1,400;1,600;1,700&family=Playfair+Display:wght@500;700&family=Oswald:wght@500;600&display=swap" rel="stylesheet">
<style>
:root{
  --page:#e6e3e1;
  --sheet:#151515;
  --sheet-edge:#232323;
  --gold:#e3b22b;
  --gold-deep:#b98a1c;
  --gold-light:#f0cd63;
  --ink:#f2f2f2;
  --muted:#c9c9c9;
}
*{box-sizing:border-box;margin:0;padding:0}
html,body{width:1200px;height:801px;overflow:hidden;background:var(--page)}
body{position:relative;font-family:"Poppins",sans-serif}

.sheet{position:absolute;width:513px;height:363px;overflow:hidden;
  background:radial-gradient(ellipse at 50% 40%,#2a2a2a 0%,var(--sheet) 70%,#0d0d0d 100%);
  box-shadow:0 6px 14px rgba(0,0,0,.25)}
.sheet--outside{left:75px;top:222px}
.sheet--inside{left:609px;top:224px}
.panel{position:absolute;top:0;height:100%}

.band{position:absolute;height:13px;transform:translateX(-50%);
  background:linear-gradient(90deg,var(--gold-deep),var(--gold-light) 50%,var(--gold-deep));
  border-radius:7px 2px 7px 2px;color:#fff;font:italic 600 7px/13px "Poppins",sans-serif;text-align:center}
.band-rule{position:absolute;height:1.5px;background:linear-gradient(90deg,transparent,var(--gold))}
.band-rule--r{background:linear-gradient(90deg,var(--gold),transparent)}
.tag{position:absolute;height:9px;padding:0 7px;background:linear-gradient(90deg,var(--gold-deep),var(--gold-light));
  border-radius:5px 1px 5px 1px;color:#fff;font:italic 600 5px/9px "Poppins",sans-serif}

.col{position:absolute;display:flex;flex-direction:column}
.item{position:relative;display:flex;align-items:baseline;color:var(--gold);font:italic 400 6.2px/8px "Poppins",sans-serif;white-space:nowrap}
.item .dot{flex:none;width:5px;height:5px;border-radius:50%;background:var(--ink);margin-right:6px;align-self:center}
.item .lead{flex:1;border-bottom:1px dashed var(--gold);margin:0 2px;transform:translateY(-2px);min-width:6px}
.item .price{flex:none}
.item .desc{position:absolute;left:11px;top:8px;font:400 3.4px/4px "Poppins",sans-serif;color:var(--muted);font-style:normal}
.item--sm{font-size:5.6px}
.item--lg{font-size:7.4px}
.item--lg .desc{left:0;top:10px;font-size:4px}

.drink-photo{position:absolute;left:160px;top:6px;width:70px;height:72px;border-radius:6px;
  background:radial-gradient(circle at 30% 60%,#b3243b,transparent 45%),radial-gradient(circle at 70% 50%,#5b2a16,transparent 50%),#2a2020}
.timetable{position:absolute;left:10px;top:300px;width:236px;height:46px;border:1px solid var(--gold);border-radius:10px}

.brand{position:absolute;left:0;width:100%;top:48px;text-align:center;color:var(--gold)}
.brand__name{font:700 34px/1 "Playfair Display",serif;letter-spacing:1px}
.brand__sub{font:600 11px/1 "Poppins",sans-serif;letter-spacing:9px;margin-top:4px;color:var(--gold)}
.address{position:absolute;top:112px;left:50%;transform:translateX(-50%);width:156px;height:11px;
  background:linear-gradient(90deg,var(--gold-deep),var(--gold-light) 50%,var(--gold-deep));border-radius:6px 2px 6px 2px;
  font:500 5.2px/11px "Playfair Display",serif;color:#fff;text-align:center;white-space:nowrap}
.oven{position:absolute;left:6px;top:132px;width:245px;height:182px;
  background:radial-gradient(ellipse at 50% 72%,#c9683a 0%,#8e2c24 18%,#3a3a3a 40%,transparent 70%),radial-gradient(ellipse at 50% 35%,#e49a2c 0%,#3a3a3a 30%,transparent 60%)}
.contact{position:absolute;top:320px;left:22px;width:214px;height:32px;display:flex;
  border-left:1.5px solid var(--gold);border-right:1.5px solid var(--gold)}
.contact__block{flex:1;text-align:center;white-space:nowrap}
.contact__block+.contact__block{border-left:1.5px solid var(--gold)}
.contact__label{display:flex;justify-content:center;align-items:center;gap:3px;font:600 6.5px/1 "Poppins",sans-serif;color:var(--gold);margin-top:4px}
.contact__value{font:500 9.5px/1 "Oswald",sans-serif;color:var(--ink);margin-top:5px;letter-spacing:.3px}
.contact__value--web{font-size:8px;letter-spacing:.8px}
.icon{width:7px;height:7px}

.details{position:absolute;color:var(--gold);font:italic 400 5.6px/10px "Poppins",sans-serif;white-space:nowrap}
.details span{display:inline-block;width:5px;height:1.5px;background:var(--ink);margin-right:6px;vertical-align:middle}
</style>
</head>
<body>

<section class="sheet sheet--outside" aria-label="Outside of the leaflet">

  <div class="panel panel--back" style="left:0;width:256px">
    <div class="col" style="left:0;top:13px;width:140px;gap:12px">
      <div class="item"><span class="dot"></span>Boissons 33cl<span class="lead"></span><span class="price">2,50 €</span><span class="desc">cola, cola zero, cola cerise, soda orange, limonade, eau, thé glacé</span></div>
      <div class="item"><span class="dot"></span>Bissons bouteille<span class="lead"></span><span class="price">5,50 €</span><span class="desc">cola, soda orange, eau pétillante, thé glacé</span></div>
      <div class="item"><span class="dot"></span>Alcools et vin<span class="lead"></span><span class="price">?????</span></div>
    </div>
    <div class="drink-photo" role="img" aria-label="Two glasses of cold drinks with ice"></div>

    <div class="band-rule" style="left:6px;top:95px;width:60px"></div>
    <div class="band" style="left:130px;top:83px;width:120px">Supplements</div>
    <div class="band-rule band-rule--r" style="left:196px;top:95px;width:54px"></div>

    <div class="tag" style="left:10px;top:108px">Fromages :</div>
    <div class="tag" style="left:97px;top:108px">Viandes :</div>
    <div class="tag" style="left:185px;top:108px">Legumes :</div>

    <div class="col" style="left:0;top:122px;width:75px;gap:4.2px">
      <div class="item item--sm"><span class="dot"></span>Mozza<span class="lead"></span><span class="price">1,50 €</span></div>
      <div class="item item--sm"><span class="dot"></span>Burrata<span class="lead"></span><span class="price">3,50 €</span></div>
      <div class="item item--sm"><span class="dot"></span>Buffala<span class="lead"></span><span class="price">5 €</span></div>
      <div class="item item--sm"><span class="dot"></span>Chevre<span class="lead"></span><span class="price">2 €</span></div>
      <div class="item item--sm"><span class="dot"></span>Ail<span class="lead"></span><span class="price">1 €</span></div>
      <div class="item item--sm"><span class="dot"></span>St Nectaire<span class="lead"></span><span class="price">2,50 €</span></div>
      <div class="item item--sm"><span class="dot"></span>Olive<span class="lead"></span><span class="price">1 €</span></div>
      <div class="item item--sm"><span class="dot"></span>Gorgonzola<span class="lead"></span><span class="price">2 €</span></div>
      <div class="item item--sm"><span class="dot"></span>Anchois<span class="lead"></span><span class="price">1,50 €</span></div>
      <div class="item item--sm"><span class="dot"></span>Parmesan<span class="lead"></span><span class="price">2,50 €</span></div>
      <div class="item item--sm"><span class="dot"></span>Ricotta<span class="lead"></span><span class="price">2 €</span></div>
      <div class="item item--sm"><span class="dot"></span>Ananas<span class="lead"></span><span class="price">2 €</span></div>
    </div>
    <div style="position:absolute;left:80px;top:122px;width:1px;height:160px;background:var(--gold)"></div>
    <div class="col" style="left:86px;top:122px;width:75px;gap:4.2px">
      <div class="item item--sm"><span class="dot"></span>Poulet<span class="lead"></span><span class="price">2,50 €</span></div>
      <div class="item item--sm"><span class="dot"></span>Viande hachee<span class="lead"></span><span class="price">2,50 €</span></div>
      <div class="item item--sm"><span class="dot"></span>Merguez<span class="lead"></span><span class="price">2,50 €</span></div>
      <div class="item item--sm"><span class="dot"></span>Jambon cuit<span class="lead"></span><span class="price">2 €</span></div>
      <div class="item item--sm"><span class="dot"></span>Lardon<span class="lead"></span><span class="price">2 €</span></div>
      <div class="item item--sm"><span class="dot"></span>Jambon parme<span class="lead"></span><span class="price">3,50 €</span></div>
      <div class="item item--sm"><span class="dot"></span>Thon<span class="lead"></span><span class="price">2 €</span></div>
      <div class="item item--sm"><span class="dot"></span>Saumon<span class="lead"></span><span class="price">3,50 €</span></div>
      <div class="item item--sm"><span class="dot"></span>Chorizo<span class="lead"></span><span class="price">2,50 €</span></div>
      <div class="item item--sm"><span class="dot"></span>Fruit de mer<span class="lead"></span><span class="price">3,50 €</span></div>
      <div class="item item--sm"><span class="dot"></span>Scampi<span class="lead"></span><span class="price">3,50 €</span></div>
      <div class="item item--sm"><span class="dot"></span>Andouillette<span class="lead"></span><span class="price">2 €</span></div>
      <div class="item item--sm"><span class="dot"></span>Jambon cru<span class="lead"></span><span class="price">2 €</span></div>
    </div>
    <div style="position:absolute;left:168px;top:122px;width:1px;height:160px;background:var(--gold)"></div>
    <div class="col" style="left:174px;top:122px;width:75px;gap:4.2px">
      <div class="item item--sm"><span class="dot"></span>Poivron<span class="lead"></span><span class="price">1,50 €</span></div>
      <div class="item item--sm"><span class="dot"></span>Champignon<span class="lead"></span><span class="price">2 €</span></div>
      <div class="item item--sm"><span class="dot"></span>Oignon<span class="lead"></span><span class="price">1,50 €</span></div>
      <div class="item item--sm"><span class="dot"></span>Câpre<span class="lead"></span><span class="price">1,50 €</span></div>
      <div class="item item--sm"><span class="dot"></span>Pomme de terre<span class="lead"></span><span class="price">2 €</span></div>
      <div class="item item--sm"><span class="dot"></span>Aubergine<span class="lead"></span><span class="price">2 €</span></div>
      <div class="item item--sm"><span class="dot"></span>Artichaud<span class="lead"></span><span class="price">1,50 €</span></div>
      <div class="item item--sm"><span class="dot"></span>Courgette<span class="lead"></span><span class="price">2 €</span></div>
      <div class="item item--sm"><span class="dot"></span>Oeuf<span class="lead"></span><span class="price">1 €</span></div>
      <div class="item item--sm"><span class="dot"></span>Roquette<span class="lead"></span><span class="price">2 €</span></div>
      <div class="item item--sm"><span class="dot"></span>Tomate cerise<span class="lead"></span><span class="price">2 €</span></div>
      <div class="item item--sm"><span class="dot"></span>Pistache<span class="lead"></span><span class="price">1 €</span></div>
    </div>

    <div class="timetable" aria-label="Space reserved for opening hours"></div>
  </div>

  <div class="panel panel--cover" style="left:256px;width:257px;border-left:1px solid var(--sheet-edge)">
    <div class="brand">
      <div class="brand__name">Vorello</div>
      <div class="brand__sub">PIZZA</div>
    </div>
    <div class="address">27 rue des tilleuls, L-3829 Dellange, Luxembourg</div>
    <div class="oven" role="img" aria-label="Line drawing of a brick pizza oven with a pepperoni pizza on a peel"></div>
    <div class="contact">
      <div class="contact__block">
        <div class="contact__label"><svg class="icon" viewBox="0 0 10 10"><circle cx="5" cy="5" r="5" fill="#e3b22b"/><path d="M3.2 2.6l1 1-.5.8c.4.8 1 1.4 1.8 1.8l.8-.5 1 1-.8 1C4.6 7.4 2.6 5.4 2.3 3.4z" fill="#151515"/></svg>CALL US :</div>
        <div class="contact__value">(+352) 26 58 40 71</div>
      </div>
      <div class="contact__block">
        <div class="contact__label"><svg class="icon" viewBox="0 0 10 10" fill="none" stroke="#e3b22b" stroke-width="1"><circle cx="5" cy="5" r="4.3"/><ellipse cx="5" cy="5" rx="2" ry="4.3"/><path d="M.7 5h8.6"/></svg>OUR WEBSITE :</div>
        <div class="contact__value contact__value--web">www.vorello-example.lu</div>
      </div>
    </div>
  </div>
</section>

<section class="sheet sheet--inside" aria-label="Inside of the leaflet">

  <div class="panel panel--pizza" style="left:0;width:260px">
    <div class="band-rule" style="left:4px;top:25px;width:66px"></div>
    <div class="band" style="left:129px;top:13px;width:118px">Pizza : Base Tomate</div>
    <div class="band-rule band-rule--r" style="left:190px;top:25px;width:66px"></div>

    <div class="col" style="left:0;top:36px;width:108px;gap:9.4px">
      <div class="item"><span class="dot"></span>Marinara<span class="lead"></span><span class="price">15 €</span><span class="desc">anchois, capres, olive, ail</span></div>
      <div class="item"><span class="dot"></span>Napolitaine<span class="lead"></span><span class="price">9,50 €</span><span class="desc">ail origan</span></div>
      <div class="item"><span class="dot"></span>Margharita<span class="lead"></span><span class="price">10 €</span><span class="desc">mozza</span></div>
      <div class="item"><span class="dot"></span>4 fromages<span class="lead"></span><span class="price">14,50 €</span><span class="desc">mozza, chevre, parmesan, gorgonzola</span></div>
      <div class="item"><span class="dot"></span>Chevre<span class="lead"></span><span class="price">15 €</span><span class="desc">mozza, jambon cuit, chevre, olive</span></div>
      <div class="item"><span class="dot"></span>Chorizo<span class="lead"></span><span class="price">15 €</span><span class="desc">mozza, chorizo, poivrons, olive</span></div>
      <div class="item"><span class="dot"></span>Vegetarienne<span class="lead"></span><span class="price">15 €</span><span class="desc">mozza, courgette, olive, poivrons, aubergine</span></div>
      <div class="item"><span class="dot"></span>3viandes<span class="lead"></span><span class="price">17,50 €</span><span class="desc">mozza, viande haché, merguez, poulet, oeuf</span></div>
      <div class="item"><span class="dot"></span>Buffala<span class="lead"></span><span class="price">15 €</span><span class="desc">mozza, buffala</span></div>
      <div class="item"><span class="dot"></span>Calzone jambon<span class="lead"></span><span class="price">14,50 €</span><span class="desc">mozza, jambon cuit, champignon</span></div>
      <div class="item"><span class="dot"></span>Calzone chorizo<span class="lead"></span><span class="price">14,50 €</span><span class="desc">mozza, chorizo, ricotta</span></div>
    </div>
    <div class="col" style="left:135px;top:36px;width:110px;gap:9.4px">
      <div class="item"><span class="dot"></span>Bambino<span class="lead"></span><span class="price">15 €</span><span class="desc">mozza, jambon, olive</span></div>
      <div class="item"><span class="dot"></span>Reine<span class="lead"></span><span class="price">9,50 €</span><span class="desc">mozza, jambon, champignon</span></div>
      <div class="item"><span class="dot"></span>Neptune<span class="lead"></span><span class="price">10 €</span><span class="desc">mozza, thon, oignon, olive</span></div>
      <div class="item"><span class="dot"></span>Poulet<span class="lead"></span><span class="price">14,50 €</span><span class="desc">mozza, poulet, poivron, oignon, champignon</span></div>
      <div class="item"><span class="dot"></span>Campagnarde<span class="lead"></span><span class="price">15 €</span><span class="desc">mozza, jambon, artichaud, champignon, oeuf</span></div>
      <div class="item"><span class="dot"></span>Mediterranienne<span class="lead"></span><span class="price">15 €</span><span class="desc">mozza, fruits de mer</span></div>
      <div class="item"><span class="dot"></span>Exotique<span class="lead"></span><span class="price">15 €</span><span class="desc">mozza, poulet, chevre, ananas</span></div>
      <div class="item"><span class="dot"></span>4 saisons<span class="lead"></span><span class="price">17,50 €</span><span class="desc">mozza, champignon, artichaud, jambon, olive</span></div>
      <div class="item"><span class="dot"></span>Scampi<span class="lead"></span><span class="price">15 €</span><span class="desc">mozza, ail, origan, scampi</span></div>
      <div class="item"><span class="dot"></span>Vorello<span class="lead"></span><span class="price">14,50 €</span><span class="desc">mozza, porcini, chorizo, mozza fumé</span></div>
    </div>

    <div class="band-rule" style="left:4px;top:243px;width:66px"></div>
    <div class="band" style="left:129px;top:231px;width:118px">Pizza : Base Crème</div>
    <div class="band-rule band-rule--r" style="left:190px;top:243px;width:66px"></div>

    <div class="col" style="left:8px;top:254px;width:100px;gap:9.5px">
      <div class="item item--lg"><span class="name">Bianca</span><span class="lead"></span><span class="price">12,50 €</span><span class="desc">mozza, jambon</span></div>
      <div class="item item--lg"><span class="name">Chèvre miel</span><span class="lead"></span><span class="price">13 €</span><span class="desc">mozza chevre frais miel</span></div>
      <div class="item item--lg"><span class="name">Umberto</span><span class="lead"></span><span class="price">14,50 €</span><span class="desc">crème gorgonzola parmesan mozza st nectaire</span></div>
      <div class="item item--lg"><span class="name">Fermiere</span><span class="lead"></span><span class="price">16 €</span><span class="desc">mozza, poulet, champignon, oignon</span></div>
      <div class="item item--lg"><span class="name">Gorgonzola:</span><span class="lead"></span><span class="price">16,50 €</span><span class="desc">mozza, lardon, oignon, gorgonzola</span></div>
    </div>
    <div class="col" style="left:135px;top:254px;width:112px;gap:9.5px">
      <div class="item item--lg"><span class="dot"></span>Moselle<span class="lead"></span><span class="price">16,50 €</span><span class="desc" style="left:11px">mozza, viande hachée, lardon, pomme de terre</span></div>
      <div class="item item--lg"><span class="dot"></span>Bauca neve<span class="lead"></span><span class="price">15,50 €</span><span class="desc" style="left:11px">mozza, burrata, andouillette</span></div>
      <div class="item item--lg"><span class="dot"></span>Raquette<span class="lead"></span><span class="price">20,50 €</span><span class="desc" style="left:11px">mozza, ricotta, jambon cru, tomate cerise</span></div>
      <div class="item item--lg"><span class="dot"></span>Mortadela<span class="lead"></span><span class="price">14,50 €</span><span class="desc" style="left:11px">mozza burrata, pistache</span></div>
      <div class="item item--lg"><span class="dot"></span>Parma<span class="lead"></span><span class="price">17 €</span><span class="desc" style="left:11px">mozza, tomate cerise, roquette, parmesan</span></div>
    </div>
  </div>

  <div class="panel panel--more" style="left:260px;width:253px">
    <div class="band" style="left:125px;top:13px;width:120px">Panini Base Creme + Mozza</div>
    <div class="band-rule band-rule--r" style="left:192px;top:25px;width:56px"></div>
    <div class="col" style="left:0;top:34px;width:92px;gap:4.5px">
      <div class="item"><span class="dot"></span>4fromages<span class="lead"></span><span class="price">7 €</span></div>
      <div class="item"><span class="dot"></span>Saumon<span class="lead"></span><span class="price">7 €</span></div>
      <div class="item"><span class="dot"></span>Merguez<span class="lead"></span><span class="price">7 €</span></div>
    </div>
    <div class="col" style="left:133px;top:34px;width:100px;gap:4.5px">
      <div class="item"><span class="dot"></span>Poulet<span class="lead"></span><span class="price">7 €</span></div>
      <div class="item"><span class="dot"></span>Jambon<span class="lead"></span><span class="price">7 €</span></div>
      <div class="item"><span class="dot"></span>Viande Hachée<span class="lead"></span><span class="price">7 €</span></div>
    </div>

    <div class="band-rule" style="left:4px;top:92px;width:56px"></div>
    <div class="band" style="left:126px;top:80px;width:120px">Salades</div>
    <div class="band-rule band-rule--r" style="left:192px;top:92px;width:56px"></div>
    <div class="col" style="left:0;top:103px;width:108px;gap:10px">
      <div class="item"><span class="dot"></span>Nicoise<span class="lead"></span><span class="price">15,50 €</span><span class="desc">tomate, thon, olive, pomme de terre</span></div>
      <div class="item"><span class="dot"></span>Norvegienne<span class="lead"></span><span class="price">16 €</span><span class="desc">tomate, saumon, oignon</span></div>
    </div>
    <div class="col" style="left:135px;top:103px;width:105px;gap:10px">
      <div class="item"><span class="dot"></span>Chevre chaud<span class="lead"></span><span class="price">16 €</span><span class="desc">tomate lardon, chevre sur toast</span></div>
      <div class="item"><span class="dot"></span>Jambon<span class="lead"></span><span class="price">16 €</span><span class="desc">jambon, roquette, parmesan</span></div>
    </div>

    <div class="band-rule" style="left:4px;top:158px;width:56px"></div>
    <div class="band" style="left:125px;top:146px;width:120px">Pates</div>
    <div class="band-rule band-rule--r" style="left:192px;top:158px;width:56px"></div>
    <div class="tag" style="left:13px;top:169px">Spaghetti :</div>
    <div class="tag" style="left:96px;top:169px">Penne :</div>
    <div class="tag" style="left:178px;top:169px">Tagliatelle :</div>
    <div class="col" style="left:0;top:183px;width:72px;gap:4px">
      <div class="item item--sm"><span class="dot"></span>4fromages<span class="lead"></span><span class="price">7 €</span></div>
      <div class="item item--sm"><span class="dot"></span>Saumon<span class="lead"></span><span class="price">7 €</span></div>
      <div class="item item--sm"><span class="dot"></span>Merguez<span class="lead"></span><span class="price">7 €</span></div>
      <div class="item item--sm"><span class="dot"></span>Merguez<span class="lead"></span><span class="price">7 €</span></div>
      <div class="item item--sm"><span class="dot"></span>Merguez<span class="lead"></span><span class="price">7 €</span></div>
    </div>
    <div style="position:absolute;left:77px;top:183px;width:1px;height:58px;background:var(--gold)"></div>
    <div class="col" style="left:82px;top:183px;width:72px;gap:4px">
      <div class="item item--sm"><span class="dot"></span>4fromages<span class="lead"></span><span class="price">7 €</span></div>
      <div class="item item--sm"><span class="dot"></span>Saumon<span class="lead"></span><span class="price">7 €</span></div>
      <div class="item item--sm"><span class="dot"></span>Merguez<span class="lead"></span><span class="price">7 €</span></div>
      <div class="item item--sm"><span class="dot"></span>Merguez<span class="lead"></span><span class="price">7 €</span></div>
      <div class="item item--sm"><span class="dot"></span>Merguez<span class="lead"></span><span class="price">7 €</span></div>
    </div>
    <div style="position:absolute;left:159px;top:183px;width:1px;height:58px;background:var(--gold)"></div>
    <div class="col" style="left:164px;top:183px;width:72px;gap:4px">
      <div class="item item--sm"><span class="dot"></span>4fromages<span class="lead"></span><span class="price">7 €</span></div>
      <div class="item item--sm"><span class="dot"></span>Saumon<span class="lead"></span><span class="price">7 €</span></div>
      <div class="item item--sm"><span class="dot"></span>Merguez<span class="lead"></span><span class="price">7 €</span></div>
      <div class="item item--sm"><span class="dot"></span>Merguez<span class="lead"></span><span class="price">7 €</span></div>
      <div class="item item--sm"><span class="dot"></span>Merguez<span class="lead"></span><span class="price">7 €</span></div>
    </div>

    <div class="tag" style="left:13px;top:250px">DETAILS :</div>
    <div class="details" style="left:0;top:261px"><span></span>Vorello : porcini, chorizo, mozza fumee<br><span></span>Saumon : creme, saumon, oignon</div>
    <div class="item" style="position:absolute;left:124px;top:265px;font:italic 600 7.2px/8px Poppins,sans-serif;color:var(--ink)"><span class="dot"></span>lasagne maison<span class="lead" style="border-color:var(--ink);width:10px"></span><span class="price">14,50€</span></div>

    <div class="band" style="left:126px;top:296px;width:120px">Desserts</div>
    <div class="band-rule band-rule--r" style="left:192px;top:308px;width:56px"></div>
    <div class="col" style="left:8px;top:317px;width:98px;gap:4.5px">
      <div class="item"><span class="dot"></span>4fromages<span class="lead"></span><span class="price">7 €</span></div>
      <div class="item"><span class="dot"></span>Saumon<span class="lead"></span><span class="price">7 €</span></div>
      <div class="item"><span class="dot"></span>Merguez<span class="lead"></span><span class="price">7 €</span></div>
    </div>
    <div class="col" style="left:142px;top:317px;width:98px;gap:4.5px">
      <div class="item"><span class="dot"></span>Poulet<span class="lead"></span><span class="price">7 €</span></div>
      <div class="item"><span class="dot"></span>Jambon<span class="lead"></span><span class="price">7 €</span></div>
      <div class="item"><span class="dot"></span>Viande Hachée<span class="lead"></span><span class="price">7 €</span></div>
    </div>
  </div>
</section>

</body>
</html>
```